A new novel about the early days of The Marlows needs a book cover design

The title of the book is A LANTERN IN WINTER
The cover should also include "a novel" and "by Tom Holloway" Those can be together or separate.
The design element I'd like to incorporate is the iconic "Dock Wall" photo of The Marlows in 1960, which I've attached below. Since we're not sure if we can get the rights to the actual photo, it's probably best if the design merely references that photo, or distorts it in an interesting way. But it should be very clear that the book is about the Marlows.
The novel is in many ways based on that photo and evokes the city of Hamburg in 1960, which was gritty, raw, and sexually charged (as were The Marlows).
The tone of the novel is romantic, passionate, and very funny - but never broad and silly.

```html
<!DOCTYPE html>
<html lang="en">
<head>
<meta charset="utf-8">
<title>A Lantern in Winter — Book Cover</title>
<link rel="stylesheet" href="https://fonts.googleapis.com/css2?family=Smooch+Sans:wght@100;300&family=Allura&display=swap">
<style>
  :root {
    --ink: #000000;
    --paper: #ffffff;
    --title: #ffffff;
    --subtitle: #9a9a9c;
    --byline: #6a6a6a;
    --amber: #f9b24a;
    --indigo: #33329a;
    --cobalt: #1778c0;
    --plum: #a01e64;
    --sky: #00aeea;
    --violet: #652d91;
  }
  * { margin: 0; padding: 0; box-sizing: border-box; }
  html, body {
    width: 1200px;
    height: 957px;
    overflow: hidden;
    background: var(--paper);
  }
  .canvas {
    position: relative;
    width: 1200px;
    height: 957px;
    background: var(--paper);
  }
  .cover {
    position: absolute;
    left: 0;
    top: 0;
    width: 686px;
    height: 957px;
    background: var(--ink);
    overflow: hidden;
  }
  .band-artwork {
    position: absolute;
    left: 0;
    top: 256px;
    width: 686px;
    height: 452px;
    background:
      linear-gradient(to bottom, rgba(0,0,0,0) 0%, rgba(0,0,0,0.15) 40%, var(--ink) 70%),
      linear-gradient(to right, var(--amber) 0%, var(--indigo) 20%, var(--cobalt) 38%, var(--plum) 60%, var(--sky) 82%, var(--violet) 100%);
  }
  .cover-type {
    position: absolute;
    left: 0;
    top: 0;
    width: 686px;
    height: 957px;
  }
  .cover-title {
    font-family: "Smooch Sans", sans-serif;
    font-weight: 100;
    font-size: 172px;
    fill: var(--title);
  }
  .cover-subtitle {
    font-family: "Smooch Sans", sans-serif;
    font-weight: 300;
    font-size: 40px;
    fill: var(--subtitle);
  }
  .cover-byline {
    font-family: "Allura", cursive;
    font-size: 92px;
    fill: var(--byline);
  }
</style>
</head>
<body>
  <main class="canvas">
    <section class="cover">
      <div class="band-artwork" role="img" aria-label="Stylised posterised scene of the Marlows performing with guitars and drums against a dock wall of brightly coloured panels"></div>
      <svg class="cover-type" viewBox="0 0 686 957" width="686" height="957">
        <text class="cover-title" x="53" y="174" textLength="550" lengthAdjust="spacingAndGlyphs">A LANTERN IN WINTER</text>
        <text class="cover-subtitle" x="268" y="240" textLength="109" lengthAdjust="spacing">A NOVEL</text>
        <text class="cover-byline" x="167" y="856" textLength="335" lengthAdjust="spacingAndGlyphs">by Tom Holloway</text>
      </svg>
    </section>
  </main>
</body>
</html>
```